Master & Realtor Did you know

I am a realtor and also a Master in Korean Martial arts, I would like to specifically market to my Karate clientele and make them aware that I am a realtor for the last 12 years in addition to being a karate instructor. also the similarities between both jobs Integrity, perseverance ,dedication, etc... also I would like to use a photo of myself on the front of the postcard that shows me in uniform and my suite attire.or I am open to a different approachRobert Reynolds

Target Market(s)

MY Karate clients

Industry/Entity Type

Real Estate Agent

Requirements
Must have
• Bullet points on the back with description of both job similarities example..
• Integrity, perseverance, focus, determination , people skills, be able to finish what I have started with the anticipated outcome.
• 33 years in teaching Martial Arts, 12 years as a professional Realtor.
• Please feel free to use your own words in description

```html
<!DOCTYPE html>
<html lang="en">
<head>
<meta charset="utf-8">
<title>Master &amp; Realtor Postcard</title>
<link rel="stylesheet" href="https://fonts.googleapis.com/css2?family=Lato:ital,wght@0,400;0,700;0,900;1,400;1,700;1,900&family=Montserrat:wght@800&display=swap">
<style>
  :root {
    --navy: #0d1a3a;
    --blue: #17a4f0;
    --sky: #6fcaf6;
    --sky-pale: #d7f0fc;
    --ink: #1d1d1f;
    --grey-line: #9a9a9a;
    --paper: #ffffff;
    --backdrop: #e9eaec;
  }
  * { box-sizing: border-box; margin: 0; padding: 0; }
  html, body { width: 902px; height: 1200px; overflow: hidden; }
  body { background: var(--backdrop); font-family: "Lato", sans-serif; color: var(--ink); position: relative; }

  .postcard { position: absolute; left: 108px; width: 686px; height: 532px; background: var(--paper); overflow: hidden; box-shadow: 0 2px 8px rgba(0,0,0,.18); }
  .postcard--front { top: 30px; }
  .postcard--back { top: 612px; }

  .front-shapes { position: absolute; inset: 0; }

  .school-mark { position: absolute; left: 20px; top: 34px; display: flex; align-items: center; gap: 6px; }
  .school-mark__dot { width: 14px; height: 14px; border-radius: 50%; background: var(--navy); }
  .school-mark__name { font-weight: 700; font-size: 12px; color: var(--navy); line-height: 1.1; width: 52px; }

  .photo-uniform { position: absolute; left: 73px; top: 20px; width: 176px; height: 252px; background: linear-gradient(180deg, #e6e6e6 0%, #2a2a2e 45%, #1a1a1e 100%); border-radius: 60px 60px 0 0; }

  .headline { position: absolute; right: 18px; top: 24px; text-align: right; }
  .headline__title { font-family: "Montserrat", sans-serif; font-weight: 800; font-size: 43px; letter-spacing: -0.5px; line-height: 1; color: var(--ink); }
  .headline__question { font-family: "Lato", sans-serif; font-weight: 400; font-size: 61px; line-height: 1.05; color: var(--blue); letter-spacing: -1px; }
  .headline__note { font-style: italic; font-weight: 700; font-size: 17px; line-height: 1.3; margin-top: 6px; color: var(--ink); }

  .agency { position: absolute; left: 18px; top: 288px; display: flex; align-items: center; gap: 8px; }
  .agency__dot { width: 16px; height: 16px; background: var(--ink); }
  .agency__name { font-size: 17px; line-height: 1.05; color: var(--ink); }
  .agency__tag { font-size: 5.5px; letter-spacing: .3px; text-transform: uppercase; margin-top: 2px; }

  .intro { position: absolute; left: 26px; top: 350px; }
  .intro__lead { font-weight: 700; font-size: 15px; color: #2a2a2a; }
  .intro__facts { font-style: italic; font-weight: 700; font-size: 21px; line-height: 1.3; color: var(--blue); margin-top: 4px; }

  .portrait-frame { position: absolute; left: 433px; top: 232px; width: 280px; height: 280px; border-radius: 50%; background: var(--blue); }
  .portrait-frame__ring { position: absolute; inset: 7px; border-radius: 50%; background: var(--navy); }
  .portrait-photo { position: absolute; inset: 17px; border-radius: 50%; background: radial-gradient(circle at 50% 30%, #c9cdd2 0%, #b6bbc1 40%, #2c2d33 75%); }

  .front-call { position: absolute; left: 32px; top: 458px; font-weight: 700; font-size: 38px; color: var(--paper); }
  .front-call__label { color: var(--blue); }

  /* back */
  .back-panel { position: absolute; left: 0; top: 0; width: 338px; height: 440px; background: linear-gradient(90deg, var(--sky-pale) 0%, var(--sky) 100%); border-right: 6px solid var(--navy); }
  .section-tag { position: absolute; left: 20px; top: 20px; padding: 4px 22px 4px 10px; background: var(--navy); color: var(--paper); font-weight: 900; font-size: 14px; border-radius: 0 12px 12px 0; }
  .traits { position: absolute; left: 20px; top: 48px; width: 290px; font-style: italic; font-weight: 900; font-size: 12.5px; line-height: 1.3; color: #24324a; }
  .similarities { position: absolute; left: 20px; top: 106px; width: 290px; list-style: none; font-size: 11.5px; line-height: 1.3; color: #1e2633; }
  .similarities li { position: relative; padding-left: 18px; margin-bottom: 3px; }
  .similarities li::before { content: ""; position: absolute; left: 0; top: 4px; width: 7px; height: 7px; border-radius: 50%; background: var(--navy); }
  .thumb { position: absolute; width: 92px; height: 92px; border-radius: 50%; border: 4px solid var(--navy); }
  .thumb--dojo { left: 303px; top: 16px; background: linear-gradient(180deg, #b7c3cf, #6e7783); }
  .thumb--house { left: 303px; top: 110px; background: linear-gradient(180deg, #9cc6e6 0%, #c8b894 55%, #6b8f4a 100%); }
  .referral { position: absolute; left: 0; top: 206px; width: 332px; height: 178px; background: #f4f6f8; border-radius: 14px; padding: 16px 36px 0 38px; }
  .referral__text { font-size: 11.5px; line-height: 1.35; color: #1e2633; }
  .referral__field { border-top: 1px solid #555; margin-top: 26px; padding-top: 5px; font-size: 10.5px; color: var(--blue); width: 258px; }
  .referral__field--second { margin-top: 22px; font-size: 9.5px; }
  .back-call { position: absolute; left: 0; top: 392px; width: 332px; height: 48px; background: var(--blue); padding: 6px 0 0 22px; font-weight: 900; font-size: 28px; color: var(--paper); }
  .back-call__label { color: var(--ink); }
  .stamp-box { position: absolute; left: 572px; top: 80px; width: 86px; height: 92px; border: 1.5px solid #333; }
  .address-line { position: absolute; left: 350px; width: 260px; border-top: 1.5px solid var(--grey-line); }
</style>
</head>
<body>

<section class="postcard postcard--front" aria-label="Postcard front">
  <svg class="front-shapes" width="686" height="532" viewBox="0 0 686 532" aria-hidden="true">
    <path d="M0 188 C 170 272 380 300 686 232 L686 244 C 380 312 170 286 0 204 Z" fill="var(--navy)"/>
    <path d="M0 182 C 170 262 380 290 686 224 L686 229 C 380 296 170 268 0 188 Z" fill="var(--blue)"/>
    <path d="M0 446 C 200 436 420 430 686 408 L686 532 L0 532 Z" fill="var(--navy)"/>
    <path d="M0 438 C 200 428 420 422 686 400" stroke="var(--navy)" stroke-width="1.5" fill="none"/>
  </svg>

  <div class="school-mark">
    <span class="school-mark__dot"></span>
    <span class="school-mark__name">Summit Karate</span>
  </div>

  <div class="photo-uniform" role="img" aria-label="Photo of the instructor standing in a black martial arts uniform, tying his belt"></div>

  <div class="headline">
    <h1 class="headline__title">MASTER &amp; REALTOR</h1>
    <p class="headline__question">Did you know?</p>
    <p class="headline__note">There are many similarities between both jobs<br>Integrity, perseverance ,dedication, etc...</p>
  </div>

  <div class="agency">
    <span class="agency__dot"></span>
    <div>
      <div class="agency__name">Hartley Crane<br>&nbsp;&nbsp;&nbsp;&nbsp;&nbsp;&nbsp;&nbsp;&nbsp;&nbsp;Real Estate</div>
      <div class="agency__tag">A boutique real estate firm with global connections</div>
    </div>
  </div>

  <div class="intro">
    <p class="intro__lead">I am a realtor and also a Master in Korean Martial arts</p>
    <p class="intro__facts">33 years in teaching Martial Arts and<br>12 years as a professional Realtor</p>
  </div>

  <div class="portrait-frame">
    <div class="portrait-frame__ring"></div>
    <div class="portrait-photo" role="img" aria-label="Portrait photo of the realtor in a dark suit with arms crossed"></div>
  </div>

  <p class="front-call"><span class="front-call__label">Call me:</span> 0123456789</p>
</section>

<section class="postcard postcard--back" aria-label="Postcard back">
  <div class="back-panel">
    <h2 class="section-tag">JOB SIMILARITIES</h2>
    <p class="traits">Integrity, perseverance, focus, determination , people skills, be able to finish what I have started with the anticipated outcome.</p>
    <ul class="similarities">
      <li>Lorem ipsum dolor sit amet, consectetuer adipiscing elit. Aenean commodo ligula eget dolor.</li>
      <li>Aenean massa. Cum sociis natoque penatibus et magnis dis parturient montes,</li>
      <li>Nascetur ridiculus mus. Donec quam felis, ultricies nec, pellentesque eu, pretium quis, sem.</li>
    </ul>
    <div class="referral">
      <p class="referral__text">Your referral of a friend or family member is the greatest compliment I can receive. I’ll work to give them the facility as yours, and you’ll receive a special thank you gift when they bring this card to their first visit.</p>
      <p class="referral__field">Referring Name</p>
      <p class="referral__field referral__field--second">New Member name</p>
    </div>
    <p class="back-call"><span class="back-call__label">Call me :</span> 0123456789</p>
  </div>
  <div class="thumb thumb--dojo" role="img" aria-label="Photo of two martial artists sparring in a dojo"></div>
  <div class="thumb thumb--house" role="img" aria-label="Photo of a suburban house with a front lawn"></div>

  <div class="stamp-box"></div>
  <div class="address-line" style="top:252px"></div>
  <div class="address-line" style="top:280px"></div>
  <div class="address-line" style="top:308px"></div>
</section>

</body>
</html>
```